Seasons of a Restless Mind - Walking Past the Tempest

I need a book cover, spine, and back cover. I need the book cover first for a book being written through tomecrafter.io. My sample shows a woman. I want a man in his 30s/40s. This is a book about me. I have suffered from bipolar disorder from adolescence to the present age of 75. I wasn't diagnosed until I was 50. Treatment has continued through the present. I'm not sure why I'm writing this, but I already have the title and subtitle for my book, but you know more than I do.
Target Market(s)
teens to 30's
Industry/Entity Type
none
Font styles to use
Serif
Requirements
Must have
- Man staring into oblivion or silhouette facing left and right Light and Dark
Nice to have
- See existing design- or man facing Left in the dark - facing right in the right
Should not have
- Woman

```html
<!DOCTYPE html>
<html lang="en">
<head>
<meta charset="utf-8">
<title>Seasons of a Restless Mind – Cover Wrap</title>
<link rel="stylesheet" href="https://fonts.googleapis.com/css2?family=Tinos:wght@400;700&family=PT+Sans:wght@400&family=Barlow:wght@700&display=swap">
<style>
  :root {
    --ink: #000000;
    --paper: #ffffff;
    --accent-red: #f10a0a;
    --placeholder-grey: #bdbdbd;
    --rule: #cfcfcf;
    --glow-white: rgba(255, 250, 245, 0.95);
    --glow-warm: rgba(236, 170, 130, 0.75);
    --shadow-blue: #0a1018;
  }
  * { margin: 0; padding: 0; box-sizing: border-box; }
  html, body {
    width: 1200px;
    height: 847px;
    overflow: hidden;
    background: var(--ink);
  }
  .cover-wrap {
    position: relative;
    width: 1200px;
    height: 847px;
    background: var(--ink);
    overflow: hidden;
    font-family: "Tinos", "Times New Roman", serif;
    color: var(--paper);
  }
  .cover-art {
    position: absolute;
    inset: 0;
    background:
      radial-gradient(ellipse 95px 230px at 905px 370px, var(--glow-white) 0%, rgba(255,245,235,0.55) 45%, rgba(0,0,0,0) 100%),
      radial-gradient(ellipse 260px 320px at 1080px 640px, var(--glow-warm) 0%, rgba(190,120,90,0.35) 45%, rgba(0,0,0,0) 100%),
      radial-gradient(ellipse 300px 420px at 900px 420px, rgba(200,150,120,0.35) 0%, rgba(0,0,0,0) 100%),
      radial-gradient(ellipse 90px 220px at 272px 360px, rgba(255,245,235,0.28) 0%, rgba(0,0,0,0) 100%),
      radial-gradient(ellipse 200px 260px at 400px 560px, rgba(150,100,80,0.25) 0%, rgba(0,0,0,0) 100%),
      linear-gradient(180deg, var(--shadow-blue) 0%, var(--ink) 100%);
  }
  .type-layer {
    position: absolute;
    inset: 0;
  }
  .back-blurb,
  .author-bio {
    position: absolute;
    font-family: "PT Sans", Arial, sans-serif;
    font-size: 16.5px;
    line-height: 27px;
    letter-spacing: 1.2px;
    text-align: justify;
    color: var(--paper);
  }
  .back-blurb { left: 37px; width: 491px; }
  .back-blurb.is-first { top: 245px; }
  .back-blurb.is-second { top: 363px; }
  .back-blurb.is-third { top: 481px; }
  .author-photo-slot {
    position: absolute;
    left: 36px;
    top: 646px;
    width: 148px;
    height: 113px;
    background: var(--placeholder-grey);
  }
  .author-bio {
    left: 202px;
    top: 637px;
    width: 326px;
  }
  .title-svg { position: absolute; inset: 0; }
  .serif-title { font-family: "Tinos", "Times New Roman", serif; fill: var(--paper); }
  .serif-title .accent { fill: var(--accent-red); }
  .author-line {
    font-family: "Barlow", Arial, sans-serif;
    font-weight: 700;
    fill: var(--paper);
  }
</style>
</head>
<body>
<main class="cover-wrap">
  <div class="cover-art" role="img" aria-label="Photograph of a man seen from behind walking out of darkness toward a glowing doorway, with warm mist rising on the right"></div>

  <section class="type-layer back-cover">
    <p class="back-blurb is-first">Lorem ipsum dolor sit amet, consectetur adipiscing elit, sed do eiusmod tempor incididunt ut labore et dolore magna aliqua. Quis ipsum suspendisse ultrices gravida. Risus commodo viverra maecenas accumsan lacus vel</p>
    <p class="back-blurb is-second">Lorem ipsum dolor sit amet, consectetur adipiscing elit, sed do eiusmod tempor incididunt ut labore et dolore magna aliqua. Quis ipsum suspendisse ultrices gravida. Risus commodo viverra maecenas accumsan lacus vel</p>
    <p class="back-blurb is-third">Lorem ipsum dolor sit amet, consectetur adipiscing elit, sed do eiusmod tempor incididunt ut labore et dolore magna aliqua. Quis ipsum suspendisse ultrices gravida. Risus commodo viverra maecenas accumsan lacus vel facilisis.</p>
    <div class="author-photo-slot" aria-label="Author photo placeholder"></div>
    <p class="author-bio">Lorem ipsum dolor sit amet, consec&shy;tetur adipiscing elit, sed do eiusmod tempor incididunt ut labore et dolore magna aliqua. Quis ipsum sus&shy;pendisse ultrices gravida. Risus com-</p>
  </section>

  <svg class="title-svg" width="1200" height="847" viewBox="0 0 1200 847" aria-label="Titles">
    <g class="serif-title back-title">
      <text x="283" y="80" text-anchor="middle"><tspan font-size="40">SEASONS</tspan><tspan font-size="29" dx="8">OF A</tspan></text>
      <text x="283" y="118" text-anchor="middle" font-size="42" textLength="488" lengthAdjust="spacing">RESTLESS <tspan class="accent">MIND</tspan></text>
      <line x1="125" y1="136" x2="445" y2="136" stroke="var(--rule)" stroke-width="1.5"/>
      <text x="283" y="182" text-anchor="middle"><tspan font-size="28">WALKING</tspan><tspan font-size="38" dx="10">PAST</tspan></text>
      <text x="283" y="224" text-anchor="middle"><tspan font-size="28">THE</tspan><tspan font-size="38" dx="10">TEMPEST</tspan></text>
    </g>

    <g class="serif-title spine-title" transform="translate(586,48) rotate(90)">
      <text x="0" y="0" textLength="577" lengthAdjust="spacing"><tspan font-size="24">SEASONS OF A </tspan><tspan font-size="31">RESTLESS </tspan><tspan class="accent" font-size="31">MIND</tspan></text>
    </g>
    <g transform="translate(607,663) rotate(90)">
      <text class="author-line" x="0" y="0" font-size="22" textLength="137" lengthAdjust="spacing">BY WALTER</text>
    </g>
    <g transform="translate(575,663) rotate(90)">
      <text class="author-line" x="0" y="0" font-size="22" textLength="137" lengthAdjust="spacing">BRENNICK</text>
    </g>

    <g class="serif-title front-title">
      <text x="918" y="112" text-anchor="middle"><tspan font-size="72">SEASONS</tspan><tspan font-size="42" dx="16">OF A</tspan></text>
      <text x="918" y="208" text-anchor="middle" font-size="104" textLength="494" lengthAdjust="spacingAndGlyphs">RESTLESS</text>
      <text class="accent" x="918" y="293" text-anchor="middle" font-size="96" letter-spacing="6">MIND</text>
      <text x="918" y="695" text-anchor="middle" font-size="56" textLength="494" lengthAdjust="spacingAndGlyphs">WALKING PAST</text>
      <text x="918" y="753" text-anchor="middle" font-size="56" textLength="490" lengthAdjust="spacingAndGlyphs">THE TEMPEST</text>
    </g>
    <text class="author-line" x="921" y="812" text-anchor="middle" font-size="23" textLength="290" lengthAdjust="spacing">BY WALTER BRENNICK</text>
  </svg>
</main>
</body>
</html>
```